Glow and Petal med spa needs an awesome eye catching billboard ad

We need a billboard ad design for a Med Spa with location sin Davenport and Windermere FL A medical spa where the beauty of nature meets the power of science to treat the whole person, mind, body and soul.

Meadowlight Renewal Med Spa is a medical spa where the beauty of nature meets the power of science to create gorgeous, youthful looking skin. Located in Davenport, Florida, but also serving Four Corners, Celebration, and Windermere, Florida, the talented professional team brings decades of experience in world-class skin care to provide holistic, science-backed aesthetic services and health coaching.

Industry/Entity Type

Spa

Colors
fbee3e
fece3e
eea4c8
e667a6
fbee3d

Requirements
Must have
• Locations in Lakeview and Palm Hollow
Phone 407-555-0192
website www.glowandpetal.example

Boards for each:
Aesthetic Treatments
Cosmetic Injectables
Lumora facial
add color vs too many earthtones, to catch the eye perhaps using yellow, something that catches the eye and stands out from the normal everyday
Thank you!!!!
Nice to have
• Boards for each:
Aesthetic Treatments
Cosmetic Injectables
Lumora facial
add color vs too many earthtones, to catch the eye
photos that match services,
Thank you!!!!

```html
<!DOCTYPE html>
<html lang="en">
<head>
<meta charset="utf-8">
<title>Meadowlight Renewal Med Spa – Cosmetic Injectables Billboard</title>
<link rel="stylesheet" href="https://fonts.googleapis.com/css2?family=PT+Sans:wght@400;700&display=swap">
<style>
  :root {
    --page: #efebe5;
    --panel-dark: #333234;
    --pink: #e667a6;
    --pink-soft: #eea4c8;
    --yellow: #fbee3e;
    --yellow-deep: #fece3e;
    --gold: #c9b07f;
    --white: #ffffff;
    --ink: #2b2b2b;
  }
  * { box-sizing: border-box; margin: 0; padding: 0; }
  html, body {
    width: 1000px; height: 1200px; overflow: hidden;
    background: var(--page);
    font-family: "PT Sans", Arial, sans-serif;
  }
  .billboard {
    position: absolute; left: 20px; top: 360px;
    width: 960px; height: 480px; overflow: hidden;
    background: var(--white);
    box-shadow: 0 18px 40px rgba(0,0,0,0.25);
  }
  .billboard__art { position: absolute; inset: 0; width: 960px; height: 480px; }
  .brand {
    position: absolute; left: 520px; top: 34px; width: 400px;
    text-align: center; color: var(--gold);
    font-weight: 400; letter-spacing: 5px; text-transform: uppercase;
  }
  .brand__name { font-size: 34px; line-height: 1.05; }
  .brand__tag { font-size: 15px; letter-spacing: 4px; margin-top: 4px; }
  .headline {
    position: absolute; left: 520px; top: 130px; width: 400px;
    text-align: center; color: var(--white);
    font-size: 50px; line-height: 1.08; font-weight: 400;
  }
  .location {
    position: absolute; left: 558px; top: 255px;
    width: 322px; height: 44px; border-radius: 22px;
    background: linear-gradient(180deg, var(--yellow) 0%, var(--yellow-deep) 100%);
    box-shadow: 0 4px 8px rgba(0,0,0,0.3);
    display: flex; align-items: center; justify-content: center; gap: 8px;
    color: var(--ink); font-size: 22px; white-space: nowrap;
  }
  .location svg { width: 16px; height: 18px; }
  .contact {
    position: absolute; left: 545px; color: var(--white);
    display: flex; align-items: center; gap: 16px; white-space: nowrap;
  }
  .contact svg { width: 30px; height: 30px; flex: none; }
  .contact--phone { top: 370px; font-size: 50px; letter-spacing: 1px; }
  .contact--web { top: 434px; font-size: 26px; }
</style>
</head>
<body>
  <section class="billboard" aria-label="Cosmetic injectables billboard">
    <svg class="billboard__art" viewBox="0 0 960 480">
      <defs>
        <linearGradient id="photoTone" x1="0" y1="0" x2="1" y2="1">
          <stop offset="0" stop-color="#ffffff"/>
          <stop offset="0.45" stop-color="#f1e0d6"/>
          <stop offset="1" stop-color="#efeceb"/>
        </linearGradient>
        <clipPath id="panelClip">
          <path d="M430 0 H960 V480 H418 C530 360 520 200 430 0 Z"/>
        </clipPath>
      </defs>
      <rect class="photo" role="img" aria-label="Photo of a woman receiving a cosmetic injection from gloved hands" x="0" y="0" width="520" height="480" fill="url(#photoTone)"/>
      <g class="wave-stripes">
        <path d="M400 0 H960 V480 H388 C500 360 490 200 400 0 Z" fill="var(--pink-soft)"/>
        <path d="M406 0 H960 V480 H394 C506 360 496 200 406 0 Z" fill="var(--white)"/>
        <path d="M412 0 H960 V480 H400 C512 360 502 200 412 0 Z" fill="var(--yellow-deep)"/>
        <path d="M424 0 H960 V480 H412 C524 360 514 200 424 0 Z" fill="var(--white)"/>
      </g>
      <path class="panel" d="M430 0 H960 V480 H418 C530 360 520 200 430 0 Z" fill="var(--panel-dark)"/>
      <g clip-path="url(#panelClip)">
        <path d="M400 322 C620 336 820 322 960 268 V480 H400 Z" fill="var(--yellow)"/>
        <path d="M400 334 C620 348 820 334 960 280 V480 H400 Z" fill="var(--white)"/>
        <path d="M400 338 C620 352 820 338 960 284 V480 H400 Z" fill="var(--pink)"/>
      </g>
    </svg>

    <div class="brand">
      <div class="brand__name">Meadowlight</div>
      <div class="brand__tag">Renewal Med Spa</div>
    </div>

    <h1 class="headline">COSMETIC<br>INJECTABLES</h1>

    <div class="location">
      <svg viewBox="0 0 16 18" aria-hidden="true">
        <path d="M8 1a5.5 5.5 0 0 0-5.5 5.5C2.5 10.5 8 15.5 8 15.5s5.5-5 5.5-9A5.5 5.5 0 0 0 8 1z" fill="none" stroke="#2b2b2b" stroke-width="1.6"/>
        <circle cx="8" cy="6.5" r="2" fill="#2b2b2b"/>
        <ellipse cx="8" cy="16.5" rx="4.5" ry="1" fill="none" stroke="#2b2b2b" stroke-width="1"/>
      </svg>
      <span>Lakeview and Palm Hollow</span>
    </div>

    <div class="contact contact--phone">
      <svg viewBox="0 0 30 30" aria-hidden="true">
        <path d="M8 4 L12 10 L9.5 12.5 C11 16 14 19 17.5 20.5 L20 18 L26 22 L23.5 26 C14 26 4 16 4 6.5 Z" fill="none" stroke="#fff" stroke-width="1.6" stroke-linejoin="round"/>
        <path d="M17 4 A9 9 0 0 1 26 13 M17 8 A5 5 0 0 1 22 13" fill="none" stroke="#fff" stroke-width="1.4"/>
      </svg>
      <span>407-555-0192</span>
    </div>

    <div class="contact contact--web">
      <svg viewBox="0 0 30 30" aria-hidden="true">
        <circle cx="15" cy="15" r="13" fill="none" stroke="#fff" stroke-width="1.4"/>
        <circle cx="15" cy="15" r="8" fill="none" stroke="#fff" stroke-width="1.4"/>
        <ellipse cx="15" cy="15" rx="3.5" ry="8" fill="none" stroke="#fff" stroke-width="1.2"/>
        <path d="M7 15 H23 M8.5 11 H21.5 M8.5 19 H21.5" stroke="#fff" stroke-width="1.2"/>
      </svg>
      <span>www.glowandpetal.example</span>
    </div>
  </section>
</body>
</html>
```